Fresh & Clean *NEW* BUSINESS CARD Needed - OPTOMETRY Clinic/Optical

High-tech optometry practice with 3 doctors seeking new business card.  We provide eye exams, sell, designer glasses/contacts/specialty eyewear and treat ocular diseases.  For our business cards, we are seeking fresh, clean, and crisp design as we grow our team (staffing change).  Simply adding doctors is making the card look busy/cluttered.
 Looking for professional, less cluttered look yet still have our logo, doctor names, phone, address, and website....If possible!  :)
Names:
Marcia Trelford, O.D.
Ned Pallister, O.D.
Oona Ferrant, O.D.
Phone: 555-014-2738
Website: www.BrightLensHub.example
Address:  417 Garnet R. Holloway, Maple Ridge, OH 00000
Ultimately we have the main business card with all doctor sames and that card has two versions  (front is always the same).  The back has two designs (1) displays next appointment time/date, (2) for "general use" (non-appointment.)    I have attached what we have used in the past.  
We also need a design template for each team member in our practice with their name, title, and email.   Those should be designed with the "general use" back (see attached).
**Open to entirely new design so don't feel obligated to keep current format.  Need new perspective!  Also including our watermark and some other design features we have consistently used in past in our portfolio.  Included are two options for logos--vertical and horizontal.
**I also would like to remove "Member of Sight Alliance" on our logo if possible**
 Other image files available upon request.

Target Market(s)

New patient & Current Patients

Industry/Entity Type

Optometry

Contact Information for Business Card

High-tech optometry practice with 3 doctors seeking new business card.  We provide eye exams, sell, designer glasses/contacts/specialty eyewear and treat ocular diseases.  For our business cards, we are seeking fresh, clean, and crisp design as we grow our team (staffing change).  Simply adding doctors is making the card look busy/cluttered.  Looking for professional, less cluttered look yet still have our logo, doctor names, phone, address, and website....If possible!  :) Names: Marcia Trelford, O.D. Ned Pallister, O.D. Oona Ferrant, O.D. Phone: 555-014-2738 Website: www.BrightLensHub.example Address:  417 Garnet R. Holloway, Maple Ridge, OH 00000 Ultimately we have the main business card with all doctor sames and that card has two versions  (front is always the same).  The back has two designs (1) displays next appointment time/date, (2) for "general use" (non-appointment.)    I have attached what we have used in the past.   We also need a design template for each team member in our practice with their name, title, and email.   Those should be designed with the "general use" back (see attached). **Open to entirely new design so don't feel obligated to keep current format.  Need new perspective!  Also including our watermark and some other design features we have consistently used in past in our portfolio.  Included are two options for logos--vertical and horizontal. **I also would like to remove "Member of Sight Alliance" on our logo if possible**  Other image files available upon request.

Font styles to use
Other font styles liked:
• We have used Montserrat / Yellowtail in the past

Colors

Designer to choose colors to be used in the design.

Requirements
Must have
• Clean & Fresh Design with Logo / Info provided in description. Horizontal orientation. **I have included the CMYK colors we currently have in our logo.
Should not have
• Cluttered

```html
<!DOCTYPE html>
<html lang="en">
<head>
<meta charset="utf-8">
<title>BrightLens Eye Studio – Business Cards</title>
<link rel="stylesheet" href="https://fonts.googleapis.com/css2?family=Montserrat:wght@400;500;600&display=swap">
<style>
  :root{
    --bg:#e9eded;
    --card:#ffffff;
    --olive:#939a45;
    --slate:#4d6573;
    --sky:#a5d8e6;
    --brown:#5c2f1a;
    --gold:#d6a625;
    --navy:#2b3a48;
    --ink:#555a5e;
    --rule:#b9bcbe;
    --badge:#c9cbcc;
  }
  *{box-sizing:border-box;margin:0;padding:0}
  html,body{width:1200px;height:900px;overflow:hidden}
  body{background:var(--bg);font-family:"Montserrat",sans-serif;color:var(--ink);position:relative}
  .card{position:absolute;left:300px;width:600px;height:343px;background:var(--card);
        box-shadow:0 6px 18px rgba(0,0,0,.12);overflow:hidden}
  .card--front{top:80px}
  .card--back{top:470px}

  .stripe{position:absolute;left:0;right:0;bottom:0;height:22px;display:flex}
  .stripe span{flex:1}
  .stripe .s1{background:var(--slate);flex:.5}
  .stripe .s2{background:var(--sky);flex:1.4}
  .stripe .s3{background:var(--olive)}
  .stripe .s4{background:var(--brown);flex:.6}
  .stripe .s5{background:var(--gold)}
  .stripe .s6{background:var(--navy);flex:2}

  /* front */
  .brand{position:absolute;left:40px;top:38px;display:flex;align-items:center;gap:16px}
  .brand__dot{width:46px;height:46px;border-radius:50%;background:var(--sky);flex:none}
  .brand__name{font-size:28px;font-weight:400;color:var(--ink);letter-spacing:.3px;white-space:nowrap}
  .partner{position:absolute;right:40px;top:47px;width:80px;height:28px;border-radius:4px;background:var(--badge)}
  .divider{position:absolute;left:40px;right:40px;top:118px;border-top:1px solid var(--rule)}
  .doctors{position:absolute;left:0;right:0;top:132px;height:92px;background:var(--olive);
           padding:12px 40px;color:#fff;font-size:16px;font-weight:500;line-height:23px}
  .contact{position:absolute;left:40px;right:40px;top:236px;display:flex;justify-content:space-between;align-items:flex-start;font-size:13px;line-height:20px}
  .contact__web{color:var(--gold);display:flex;align-items:center;gap:8px}
  .contact__row{display:flex;align-items:center;gap:8px}
  .icon{width:16px;height:16px;flex:none}

  /* back */
  .appt__band{position:absolute;left:0;right:0;top:0;height:62px;background:var(--olive);color:#fff;
              font-size:24px;font-weight:400;padding:16px 40px}
  .back-brand{position:absolute;left:30px;top:110px;display:flex;flex-direction:column;align-items:center;gap:10px;width:180px}
  .back-brand .brand__dot{width:80px;height:80px}
  .back-brand .brand__name{font-size:14px;text-align:center}
  .fields{position:absolute;left:230px;right:40px;top:96px}
  .field{border-bottom:1px solid var(--rule);height:42px}
  .field-row{display:flex}
  .field-row .field{flex:1;font-size:12px;padding-top:24px}
  .field-row .field + .field{border-left:1px solid var(--rule);padding-left:10px}
  .notice{position:absolute;left:230px;right:40px;top:250px;font-size:11px;font-weight:500;letter-spacing:.6px;line-height:17px;text-transform:uppercase}
</style>
</head>
<body>

<section class="card card--front">
  <div class="brand">
    <span class="brand__dot"></span>
    <span class="brand__name">BrightLens Eye Studio</span>
  </div>
  <div class="partner" role="img" aria-label="Partner membership badge"></div>
  <div class="divider"></div>
  <div class="doctors">
    <p>Marcia Trelford, O.D.</p>
    <p>Ned Pallister, O.D.</p>
    <p>Oona Ferrant, O.D.</p>
  </div>
  <div class="contact">
    <div class="contact__address">
      <p>417 Garnet R. Holloway,</p>
      <p>Maple Ridge, OH 00000</p>
    </div>
    <div>
      <p class="contact__row">
        <svg class="icon" viewBox="0 0 16 16"><circle cx="8" cy="8" r="8" fill="#d6a625"/><path d="M5 4.5l1.6-.3.8 2-1 .8a5 5 0 0 0 2.6 2.6l.8-1 2 .8-.3 1.6c-3.6.2-6.7-2.9-6.5-6.5z" fill="#fff"/></svg>
        555-014-2738
      </p>
      <p class="contact__web">
        <svg class="icon" viewBox="0 0 16 16"><circle cx="8" cy="8" r="8" fill="#d6a625"/><circle cx="8" cy="8" r="4.5" fill="none" stroke="#fff" stroke-width="1"/><path d="M3.5 8h9M8 3.5c-2 2.5-2 6.5 0 9M8 3.5c2 2.5 2 6.5 0 9" fill="none" stroke="#fff" stroke-width="1"/></svg>
        www.BrightLensHub.example
      </p>
    </div>
  </div>
  <div class="stripe"><span class="s1"></span><span class="s2"></span><span class="s3"></span><span class="s4"></span><span class="s5"></span><span class="s6"></span></div>
</section>

<section class="card card--back">
  <div class="appt__band">Your Next Appoinment</div>
  <div class="back-brand">
    <span class="brand__dot"></span>
    <span class="brand__name">BrightLens Eye Studio</span>
  </div>
  <div class="fields">
    <div class="field"></div>
    <div class="field"></div>
    <div class="field-row">
      <div class="field">Date</div>
      <div class="field">Time</div>
    </div>
  </div>
  <p class="notice">If your unable to keep your appoinment<br>kindly give us 24 hour notice</p>
  <div class="stripe"><span class="s1"></span><span class="s2"></span><span class="s3"></span><span class="s4"></span><span class="s5"></span><span class="s6"></span></div>
</section>

</body>
</html>
```